Tri-Fold Behavioral Health (Addiction) Agency Brochure

We need an updated and refreshed brochure design for our Residential Treatment Facilities. These facilities provide residential comprehensive treatment for those struggling with drug and alcohol addiction along with those who are dually diagnosed with mental health issues as well. We are starting with this brochure but plan to have our other brochures "match" the design and will submit that following completion of this design. I have attached a "Brochure Areas" document that is numbered and corresponds to the brochure areas of our current brochure. We have modified the wording in each of these areas so the wording in the attached word document is what needs to go on the design (not the words in the attached pictures of our current brochure). We want something that is a professional design look. The front page of the brochure needs to have our main agency Logo/Name: Maple Hollow Behavioral Health Partners (logo attached). The back page we would like to have the two locations listed with the address (possible map if able). The first is called: The Harbor at Maple Hollow - located at 7214 Tolliver Lane, Frazeysburg OH 43829. The Second Facility is called: The Brennick at Maple Hollow - located at 618 Garvin St, Zanesville OH 43708. I have also attached some pictures of our facilities that can be used. They all don't have to be used and we would still like some stock photos of "people" or group counseling, etc.

Requirements
Must have
• Need final design file to be publisher or word along with pdf and or other print type file.
Nice to have
• I have also attached the current booth design photo that we are using to possibly match design look.

```html
<!DOCTYPE html>
<html lang="en">
<head>
<meta charset="utf-8">
<title>Maple Hollow Residential Treatment Brochure</title>
<link rel="stylesheet" href="https://fonts.googleapis.com/css2?family=Open+Sans:wght@400;600;700;800&family=Cinzel:wght@400;600&display=swap">
<style>
:root{
  --backdrop:#f7c93b;
  --navy:#22303f;
  --gold:#f6c531;
  --paper:#ffffff;
  --fold:#e6e7e9;
  --ink:#22303f;
  --body-ink:#2b2f35;
}
*{margin:0;padding:0;box-sizing:border-box}
html,body{width:1200px;height:1200px;overflow:hidden;background:var(--backdrop)}
body{position:relative;font-family:"Open Sans",Arial,sans-serif;color:var(--body-ink)}
.spread{position:absolute;left:274px;width:652px;height:462px;background:var(--paper);overflow:hidden}
.spread--inside{top:74px}
.spread--outside{top:578px}
.spread > svg.shapes{position:absolute;left:0;top:0;width:652px;height:462px}
.abs{position:absolute}
.photo{position:absolute}
.heading{font-weight:700;color:var(--ink);line-height:1.1}
.body-copy{font-size:7.3px;line-height:1.36}
.fold-shade{position:absolute;top:0;height:100%;width:219px;left:433px;background:linear-gradient(90deg,#fff 0%,#fff 55%,var(--fold) 100%)}
.fold-shade--mid{left:215px;width:218px}
.bullets{list-style:none;font-size:7.3px;font-weight:700;color:var(--ink);line-height:1.36}
.bullets li{padding-left:13px;position:relative}
.bullets li::before{content:"";position:absolute;left:2px;top:4px;width:2.4px;height:2.4px;border-radius:50%;background:var(--ink)}
.gold-bar{position:absolute;background:var(--gold)}
.navy-bar{position:absolute;background:var(--navy)}

/* inside spread */
.experience-title{left:16px;top:158px;font-size:18.5px}
.experience-copy{left:16px;top:183px;width:192px}
.diagnosis-title{left:236px;top:341px;font-size:18px;color:#fff}
.diagnosis-copy{left:236px;top:364px;width:196px;color:#fff}
.programming-title{left:448px;top:19px;font-size:18.5px}
.programming-copy{left:448px;top:45px;width:194px}
.programming-list{left:448px;top:112px}
.groups-title{left:447px;top:195px;font-size:17px;font-weight:400}
.groups-list{left:448px;top:214px}

/* outside spread */
.help-card{left:22px;top:192px;width:176px;height:147px;background:var(--gold);padding:8px 4px 0 3px}
.help-card .heading{font-size:18px;margin-bottom:8px}
.help-card .body-copy{font-size:7.2px;line-height:1.39}
.location{position:absolute;left:233px;display:flex;gap:7px}
.location svg{width:11px;height:15px;margin-top:6px;flex:none}
.location p{font-size:10.2px;font-weight:700;color:var(--ink);line-height:1.35;text-transform:uppercase}
.map{position:absolute;width:128px;height:128px;border-radius:50%;overflow:hidden}
.map-fill{position:absolute;inset:7px;border-radius:50%;background:radial-gradient(circle at 45% 45%,#f4f4f2 0%,#e6e7e4 80%)}
.brand-block{left:450px;top:100px;width:179px;height:86px;background:var(--gold);display:flex;flex-direction:column;align-items:center;justify-content:center;gap:3px;padding-top:18px}
.brand-mark{width:14px;height:14px;border-radius:50%;background:var(--navy);margin-bottom:6px}
.brand-name{font-family:"Cinzel",Georgia,serif;font-weight:400;color:var(--navy);text-align:center;letter-spacing:.5px;line-height:1.05}
.brand-name .lead{display:block;font-size:17px}
.brand-name .sub{display:block;font-size:7px;letter-spacing:.6px}
.facility-tag{left:450px;top:393px;width:179px;height:35px;background:var(--navy);color:#fff;font-family:"Cinzel",Georgia,serif;font-weight:400;font-size:11px;letter-spacing:2px;text-align:center;line-height:1.2;display:flex;align-items:center;justify-content:center;text-transform:uppercase}
</style>
</head>
<body>

<!-- Inside spread -->
<section class="spread spread--inside">
  <div class="fold-shade"></div>
  <svg class="shapes" viewBox="0 0 652 462" aria-hidden="true">
    <polygon points="130,0 215,0 215,110" fill="var(--navy)"/>
    <polygon points="108,462 215,462 215,330" fill="var(--navy)"/>
    <rect x="215" y="0" width="218" height="462" fill="var(--navy)"/>
    <polygon points="215,140 300,225 215,310" fill="#fff"/>
    <polygon points="324,86 434,202 324,346 192,218" fill="none" stroke="var(--gold)" stroke-width="0.8"/>
    <polygon points="414,210 433,192 433,230" fill="var(--gold)"/>
  </svg>

  <div class="photo" role="img" aria-label="Photo of a garden patio with a statue and a gazebo at the facility" style="left:16px;top:22px;width:190px;height:113px;background:linear-gradient(160deg,#c9cfc3 0%,#6f8f4e 55%,#3d5a2a 100%)"></div>
  <div class="gold-bar" style="left:16px;top:135px;width:190px;height:7px"></div>

  <h2 class="heading abs experience-title">The Experience</h2>
  <p class="body-copy abs experience-copy">Residential Treatment at Maple Hollow offers intensive structured treatment services for men and women suffering from substance abuse disorders in a 24-hour medically monitored long-term residential treatment facility.<br>Our treatment facilities offer clients the ability to feel welcomed, accepted and supported in a retreat like setting. Our multi-disciplinary team consists of Physicians, Therapists, Nurses, Case Managers, and other Recovery Support Specialists, allowing for each individual's physical, social, mental, and emotional development.</p>

  <div class="photo" role="img" aria-label="Photo of wooden lawn chairs around a fire pit on the grounds" style="left:16px;top:338px;width:190px;height:92px;background:linear-gradient(180deg,#7f9a6a 0%,#5d6a4a 45%,#6b5a48 100%);clip-path:polygon(0 0,100% 0,100% 62%,84% 100%,0 100%)"></div>

  <svg class="abs" style="left:226px;top:120px" width="196" height="195" viewBox="0 0 196 195" role="img" aria-label="Photo of a counselor speaking with a client in a bright office">
    <defs><linearGradient id="sessionTone" x1="0" y1="0" x2="1" y2="1"><stop offset="0" stop-color="#eef2f5"/><stop offset="0.6" stop-color="#a9bccb"/><stop offset="1" stop-color="#4b5d70"/></linearGradient></defs>
    <polygon points="98,0 196,98 98,195 0,98" fill="url(#sessionTone)"/>
  </svg>

  <h2 class="heading abs diagnosis-title">Dual Diagnosis</h2>
  <p class="body-copy abs diagnosis-copy">It is an unfortunate reality that many individuals who struggle with addiction are also faced with mental illness. Our residential treatment programs support dually-diagnosed individuals by providing onsite psychiatric evaluations, regular psychiatric follow-ups, medication management, and therapy services aimed at treating these symptoms as a part of the client's individualized treatment plan.</p>

  <h2 class="heading abs programming-title">Our Programming</h2>
  <p class="body-copy abs programming-copy">Residential treatment programing provides comprehensive treatment for those struggling with drug and alcohol addiction along with those who are dually diagnosed with mental health issues as well. Residents will be able to experience an evidence-based program model inclusive of:</p>
  <ul class="bullets abs programming-list">
    <li>Comprehensive Evaluations</li>
    <li>Treatment Team Collaboration</li>
    <li>Medication Management</li>
    <li>Aftercare Planning</li>
    <li>Individual Therapy</li>
    <li>Family Therapy</li>
    <li>Group</li>
  </ul>
  <h3 class="heading abs groups-title">Groups</h3>
  <ul class="bullets abs groups-list">
    <li>Psychoeducational</li>
    <li>Psychotherapy</li>
    <li>Health &amp; Wellness</li>
    <li>Independent Living Skills</li>
    <li>Peer-Led (AA/NA)</li>
    <li>Grief &amp; Loss</li>
    <li>Codependency</li>
    <li>Stress Management</li>
  </ul>
  <div class="navy-bar" style="left:446px;top:306px;width:95px;height:6px"></div>
  <div class="gold-bar" style="left:541px;top:306px;width:99px;height:6px"></div>
  <div class="photo" role="img" aria-label="Photo of a group counseling circle of young adults" style="left:446px;top:312px;width:194px;height:130px;background:linear-gradient(135deg,#e3e8ec 0%,#8fa4b6 50%,#3a4a5c 100%)"></div>
</section>

<!-- Outside spread -->
<section class="spread spread--outside">
  <div class="fold-shade fold-shade--mid"></div>
  <div class="fold-shade"></div>
  <svg class="shapes" viewBox="0 0 652 462" aria-hidden="true">
    <rect x="0" y="0" width="215" height="462" fill="var(--navy)"/>
    <polygon points="374,0 433,0 433,55" fill="var(--navy)"/>
    <polygon points="433,0 652,0 652,48 597,100 485,100 433,45" fill="var(--navy)"/>
    <polygon points="520,74 548,74 534,89" fill="var(--gold)"/>
    <polygon points="216,28 228,40 216,52 204,40" fill="var(--gold)"/>
  </svg>

  <svg class="abs" style="left:0;top:0" width="250" height="192" viewBox="0 0 250 192" role="img" aria-label="Photo of a man raising his arms in a sunlit field">
    <defs><linearGradient id="fieldTone" x1="0" y1="0" x2="0" y2="1"><stop offset="0" stop-color="#eef0ee"/><stop offset="0.55" stop-color="#cfd3cf"/><stop offset="1" stop-color="#9a8a5a"/></linearGradient></defs>
    <polygon points="70,0 142,0 250,110 215,192 0,192 0,70" fill="url(#fieldTone)"/>
  </svg>

  <div class="abs help-card">
    <h2 class="heading">Help For Addiction</h2>
    <p class="body-copy">Recovering from an can be a long and difficult process; but it is also one of the most important things that you will do in your life. And while only one person can deide to make the change, it is anything but a solitary process. Freedom from addiction can move your life forward in powerful ways. Better health, stronger relationships, steady employment and living with purpose – these are among the rewards of recovery. Maple Hollow is here to help!</p>
  </div>

  <svg class="abs" style="left:40px;top:355px" width="190" height="107" viewBox="0 0 190 107" role="img" aria-label="Photo of a smiling woman with arms stretched wide">
    <polygon points="10,107 30,20 190,0 110,107" fill="#e9e4de"/>
  </svg>

  <div class="map" style="left:255px;top:52px" role="img" aria-label="Street map showing The Harbor at Maple Hollow">
    <svg width="128" height="128" viewBox="0 0 128 128" style="position:absolute;inset:0"><path d="M4,64 A60,60 0 0 1 124,64" fill="none" stroke="var(--navy)" stroke-width="7"/><path d="M124,64 A60,60 0 0 1 4,64" fill="none" stroke="var(--gold)" stroke-width="7"/></svg>
    <div class="map-fill"></div>
  </div>
  <div class="location" style="top:193px">
    <svg viewBox="0 0 11 15" aria-hidden="true"><path d="M5.5 0C2.5 0 0 2.4 0 5.4 0 9.4 5.5 15 5.5 15S11 9.4 11 5.4C11 2.4 8.5 0 5.5 0z" fill="var(--gold)"/><circle cx="5.5" cy="5.4" r="2" fill="#fff"/></svg>
    <p>The Harbor at Maple Hollow<br>located at 7214 Tolliver Lane,<br>Frazeysburg OH 43829</p>
  </div>

  <div class="map" style="left:255px;top:247px" role="img" aria-label="Street map showing The Brennick at Maple Hollow">
    <svg width="128" height="128" viewBox="0 0 128 128" style="position:absolute;inset:0"><path d="M4,64 A60,60 0 0 1 124,64" fill="none" stroke="var(--navy)" stroke-width="7"/><path d="M124,64 A60,60 0 0 1 4,64" fill="none" stroke="var(--gold)" stroke-width="7"/></svg>
    <div class="map-fill"></div>
  </div>
  <div class="location" style="top:389px">
    <svg viewBox="0 0 11 15" aria-hidden="true"><path d="M5.5 0C2.5 0 0 2.4 0 5.4 0 9.4 5.5 15 5.5 15S11 9.4 11 5.4C11 2.4 8.5 0 5.5 0z" fill="var(--gold)"/><circle cx="5.5" cy="5.4" r="2" fill="#fff"/></svg>
    <p>The Brennick at Maple Hollow<br>located at 618 Garvin St,<br>Zanesville OH 43708</p>
  </div>

  <div class="abs brand-block">
    <span class="brand-mark" aria-hidden="true"></span>
    <p class="brand-name"><span class="lead">Maple Hollow</span><span class="sub">Behavioral Health Partners</span></p>
  </div>
  <div class="photo" role="img" aria-label="Photo of the brick residential facility with a white porch and lawn" style="left:450px;top:186px;width:179px;height:133px;background:linear-gradient(180deg,#e7ecef 0%,#9a6d5c 40%,#7d5546 62%,#4f7a3a 78%,#3d6a2d 100%)"></div>
  <div class="gold-bar" style="left:450px;top:319px;width:179px;height:7px"></div>
  <div class="abs facility-tag">The Harbor<br>at Maple Hollow</div>
</section>

</body>
</html>
```